Company Letter head for real estate company

need company letter head

You can use the logo that I submitted. no need to create a new one

• must have my address on it..38642 MARLOWE, CANTON, MI 48203-1957, INFO@WRKMB.CA

```html
<!DOCTYPE html>
<html lang="en">
<head>
<meta charset="utf-8">
<title>Wrenmark Letterhead</title>
<link href="https://fonts.googleapis.com/css2?family=Open+Sans:wght@400;600&family=Lato:wght@400;700&display=swap" rel="stylesheet">
<style>
  :root {
    --backdrop: #dcdfe6;
    --paper: #ffffff;
    --ink: #555555;
    --ink-strong: #444444;
    --brand-dark: #222222;
    --brand-green: #5a8a00;
    --leaf-green: #7fb82a;
    --footer-text: #ffffff;
  }
  html, body {
    margin: 0;
    padding: 0;
    width: 1062px;
    height: 1200px;
    overflow: hidden;
    background: var(--backdrop);
  }
  .letterhead {
    position: absolute;
    left: 234px;
    top: 260px;
    width: 594px;
    height: 767px;
    background: var(--paper);
    font-family: "Open Sans", Arial, sans-serif;
    color: var(--ink);
    overflow: hidden;
  }
  .brand {
    position: absolute;
    top: 32px;
    left: 0;
    width: 100%;
    display: flex;
    justify-content: center;
    align-items: center;
    gap: 8px;
  }
  .brand-dot {
    width: 14px;
    height: 14px;
    border-radius: 50%;
    background: var(--leaf-green);
  }
  .brand-name {
    font-family: "Open Sans", Arial, sans-serif;
    font-weight: 600;
    font-size: 24px;
    letter-spacing: 1px;
    color: var(--brand-dark);
  }
  .block {
    position: absolute;
    left: 56px;
    width: 481px;
    font-size: 9.6px;
    margin: 0;
  }
  .issue-date { top: 150px; }
  .recipient { top: 174px; line-height: 11.7px; }
  .salutation { top: 240px; }
  .body-text p {
    margin: 0;
    font-size: 9.4px;
    line-height: 17.2px;
    text-align: justify;
    hyphens: auto;
    -webkit-hyphens: auto;
  }
  .para-1 { top: 273px; }
  .para-2 { top: 376px; }
  .para-3 { top: 445px; }
  .closing { top: 532px; }
  .signature {
    position: absolute;
    left: 56px;
    top: 558px;
    width: 136px;
    height: 16px;
    background: linear-gradient(90deg, #e9e9e9, #f3f3f3);
  }
  .signer-name {
    top: 582px;
    font-size: 11.8px;
    font-weight: 600;
    color: var(--ink-strong);
  }
  .signer-title { top: 602px; }
  .footer-band {
    position: absolute;
    left: 0;
    bottom: 0;
    width: 100%;
    height: 36px;
    background: var(--brand-green);
    font-family: "Lato", Arial, sans-serif;
    color: var(--footer-text);
    font-size: 11px;
    line-height: 36px;
    white-space: nowrap;
  }
  .footer-band .contact {
    position: absolute;
    left: 48px;
    width: 452px;
    text-align: left;
    z-index: 2;
  }
  .footer-band b { font-weight: 700; }
  .tree-art {
    position: absolute;
    left: 507px;
    top: 638px;
    width: 87px;
    height: 129px;
    background: linear-gradient(180deg, #6f9a12, #5a8a00);
    border-radius: 44px 44px 0 0;
    z-index: 1;
  }
</style>
</head>
<body>
  <main class="letterhead">
    <header class="brand">
      <span class="brand-dot"></span>
      <span class="brand-name">WRENMARK</span>
    </header>

    <p class="block issue-date">Issuing Date: May 5, 2018</p>
    <p class="block recipient">Name Of Employee Mr. XYZABC<br>Address of Employee<br>Address Line 2 etc..</p>
    <p class="block salutation">Dear Mr.XYZABC</p>

    <div class="block body-text para-1"><p>Lorem Ipsum has been the industry's standard dummy text ever since the 1500s, when an unknown printer took a galley of type and scrambled it to make a type specimen book. It has survived not only five centuries, but also the leap into electronic typesetting, remaining essentially unchanged. It was popularised in the 1960s with the release of Letraset sheets containing Lorem Ipsum passages, and more recently with desktop publishing software like Aldus PageMaker including versions of Lorem Ipsum.</p></div>
    <div class="block body-text para-2"><p>Lorem Ipsum is simply dummy text of the printing and typesetting industry. Lorem Ipsum has been the industry's standard dummy text ever since the 1500s, when an unknown printer took a galley of type and scrambled it to make a type specimen book.</p></div>
    <div class="block body-text para-3"><p>It has survived not only five centuries, but also the leap into electronic typesetting, remaining essentially unchanged. It was popularised in the 1960s with the release of Letraset sheets containing Lorem IpsumIpsum passages.</p></div>

    <p class="block closing">Yours Sincerely</p>
    <div class="signature" role="img" aria-label="Handwritten signature of Marcus Hale"></div>
    <p class="block signer-name">Marcus Hale</p>
    <p class="block signer-title">Managing Director</p>

    <footer class="footer-band">
      <span class="contact"><b>P:</b> 48203-1957 <b>| E:</b> info@wrkmb.ca <b>|</b> <b>W:</b> www.wrkmb.ca | 38642 MARLOWE, CANTON, MI</span>
    </footer>
    <div class="tree-art" role="img" aria-label="Green pine tree silhouettes decoration"></div>
  </main>
</body>
</html>
```